Real Estate Team Business Card

We need a business card designed for our real estate team called "Larkspur Realty Group". We would like to receive a final format that would allow us to edit the contact information for new employees as they are added to our team. The difficult part of the design is that we will need to have two logos on the card - both our team name logo for "Larkspur Realty Group" and our company logo for "Corvane Real Estate". Most emphasis should be given to the team logo - maybe double the size of our company logo. (we just have to have the company logo somewhere on the card for legal purposes) The design should somehow illustrate we work in real estate, but still use the beehive/bee concept as a lot of our marketing will involve "bee" sayings. We would also like to use the tagline: "find out what all the buzz is about". We also need to use the "fair housing" logo and "realtor" logos. These can both be small like the company logo.
Target Market(s)
Real Estate
Industry/Entity Type
Real Estate Agent
Contact Information for Business Card
Name: Dylan Marsh Title: Realtor Phone: 801-555-0172 Email: dylan@larkspurrealtrygroup.com Website: www.larkspurrealtygroup.com Facebook: fb/me/larkspurrealtygroup Twitter: @LarkspurRltyGrp
Colors
Designer to choose colors to be used in the design.
Requirements
Must have
- Contact information. Larkspur Realty Group Logo. Corvane Real Estate Logo. Realtor logo. Fair Housing Logo. Tagline: "find out what all the buzz is about".
Nice to have
- It would be nice to illustrate that we work in real estate. It would also be nice to somehow incorporate bees or play off of our beehive logo. We will do a lot of marking using sayings like "let us bee the solution" or "real estate meant to bee" etc.

```html
<!DOCTYPE html>
<html lang="en">
<head>
<meta charset="utf-8">
<title>Larkspur Realty Group – Business Card</title>
<link rel="stylesheet" href="https://fonts.googleapis.com/css2?family=Josefin+Sans:wght@400;600;700&display=swap">
<style>
  :root {
    --backdrop: #9c9c9c;
    --card: #000000;
    --honey: #ffd400;
    --white: #ffffff;
    --corvane-blue: #1f6fc9;
  }
  * { margin: 0; padding: 0; box-sizing: border-box; }
  html, body { width: 1200px; height: 1000px; overflow: hidden; }
  body {
    background: var(--backdrop);
    position: relative;
    font-family: "Josefin Sans", sans-serif;
  }
  .card {
    position: absolute;
    width: 437px;
    height: 728px;
    background: var(--card);
    text-align: center;
  }
  .card-front { left: 103px; top: 135px; }
  .card-back  { left: 608px; top: 136px; }

  /* front */
  .brand-square {
    position: absolute;
    left: 188px; top: 62px;
    width: 60px; height: 60px;
    background: var(--honey);
  }
  .brand-name {
    position: absolute;
    left: 0; right: 0; top: 196px;
    color: var(--white);
    font-weight: 400;
    font-size: 50px;
    letter-spacing: 7px;
    line-height: 1;
  }
  .brand-sub {
    position: absolute;
    left: 86px; right: 86px; top: 250px;
    display: flex; align-items: center; gap: 10px;
    color: var(--white);
    font-weight: 400;
    font-size: 18px;
    letter-spacing: 3px;
    white-space: nowrap;
  }
  .brand-sub::before, .brand-sub::after {
    content: ""; flex: 1; height: 2px; background: var(--white);
  }
  .tagline {
    position: absolute;
    left: 0; right: 0; top: 285px;
    color: var(--honey);
    font-weight: 600;
    font-size: 12.5px;
    text-transform: uppercase;
  }
  .company-name {
    position: absolute;
    left: 0; right: 0; top: 646px;
    color: var(--corvane-blue);
    font-weight: 400;
    line-height: 1;
  }
  .company-name .word { display: block; font-size: 30px; }
  .company-name .suffix { display: block; font-size: 7px; margin-top: 4px; padding-left: 70px; letter-spacing: 0.5px; }

  /* back */
  .team-mark {
    position: absolute;
    left: 0; right: 0; top: 160px;
    display: flex; flex-direction: column; align-items: center; gap: 18px;
    color: var(--honey);
    font-weight: 600;
  }
  .team-mark .square { width: 70px; height: 70px; background: var(--honey); }
  .team-mark .word { font-size: 30px; letter-spacing: 4px; line-height: 1.15; }
  .agent-name {
    position: absolute;
    left: 0; right: 0; top: 408px;
    color: var(--honey);
    font-family: "Josefin Sans", sans-serif;
    font-weight: 600;
    font-size: 29px;
    letter-spacing: 0.5px;
    line-height: 1;
  }
  .contact-icons {
    position: absolute;
    left: 0; right: 0; top: 489px;
    display: flex; justify-content: center; gap: 9px;
  }
  .contact-icons svg { width: 29px; height: 29px; }
  .contact-list {
    position: absolute;
    left: 0; right: 0; top: 527px;
    list-style: none;
    color: var(--white);
    font-size: 17px;
    line-height: 26px;
  }
  .badges {
    position: absolute;
    left: 0; right: 0; top: 672px;
    display: flex; justify-content: center; gap: 16px;
  }
  .badge { width: 20px; height: 22px; background: var(--white); }
</style>
</head>
<body>
  <section class="card card-front">
    <div class="brand-square"></div>
    <div class="brand-name">LARKSPUR</div>
    <div class="brand-sub">REALTY GROUP</div>
    <p class="tagline">Find out what all the buzz is about</p>
    <div class="company-name">
      <span class="word">Corvane</span>
      <span class="suffix">REAL ESTATE</span>
    </div>
  </section>

  <section class="card card-back">
    <div class="team-mark">
      <div class="square"></div>
      <div class="word">LARKSPUR<br>REALTY GROUP</div>
    </div>
    <h1 class="agent-name">DYLAN MARSH</h1>

    <div class="contact-icons">
      <svg viewBox="0 0 30 30" aria-label="Phone">
        <circle cx="15" cy="15" r="13.5" fill="none" stroke="#ffd400" stroke-width="1.6"/>
        <path d="M10 9.5c1-1 2-1 2.5 0l1 2c.3.7 0 1.2-.6 1.6-.5.3-.4.8 0 1.5l1.6 1.7c.6.5 1 .5 1.4 0 .5-.6 1-.8 1.6-.5l2 1c1 .5.9 1.5 0 2.4-2 2-4.6 1-7.3-1.7S8 11.5 10 9.5z" fill="#ffd400"/>
      </svg>
      <svg viewBox="0 0 30 30" aria-label="Email">
        <circle cx="15" cy="15" r="13.5" fill="none" stroke="#ffd400" stroke-width="1.6"/>
        <rect x="8.5" y="10" width="13" height="10" fill="none" stroke="#ffd400" stroke-width="1.6"/>
        <path d="M8.5 10l6.5 5.5 6.5-5.5" fill="none" stroke="#ffd400" stroke-width="1.6"/>
      </svg>
      <svg viewBox="0 0 30 30" aria-label="Website">
        <circle cx="15" cy="15" r="13.5" fill="none" stroke="#ffd400" stroke-width="1.6"/>
        <circle cx="15" cy="15" r="7" fill="none" stroke="#ffd400" stroke-width="1.4"/>
        <ellipse cx="15" cy="15" rx="3" ry="7" fill="none" stroke="#ffd400" stroke-width="1.2"/>
        <path d="M8 15h14M9 11.5h12M9 18.5h12" stroke="#ffd400" stroke-width="1.2"/>
      </svg>
      <svg viewBox="0 0 30 30" aria-label="Social profile link">
        <circle cx="15" cy="15" r="13.5" fill="none" stroke="#ffd400" stroke-width="1.6"/>
        <path d="M11 15l8-4.5M11 15l8 4.5" stroke="#ffd400" stroke-width="1.5"/>
        <circle cx="10.5" cy="15" r="2.4" fill="#ffd400"/>
        <circle cx="19.5" cy="10.3" r="2.4" fill="#ffd400"/>
        <circle cx="19.5" cy="19.7" r="2.4" fill="#ffd400"/>
      </svg>
      <svg viewBox="0 0 30 30" aria-label="Social handle">
        <circle cx="15" cy="15" r="13.5" fill="none" stroke="#ffd400" stroke-width="1.6"/>
        <circle cx="15" cy="15" r="2.8" fill="none" stroke="#ffd400" stroke-width="1.6"/>
        <path d="M17.8 12.5v3.6c0 1.3 2.6 1.6 3-.4.9-4.3-2.3-7-5.8-7a6.3 6.3 0 1 0 3.5 11.5" fill="none" stroke="#ffd400" stroke-width="1.6" stroke-linecap="round"/>
      </svg>
    </div>

    <ul class="contact-list">
      <li>801-555-0172</li>
      <li>info@dylan@larkspurrealtygroup.com</li>
      <li>www.larkspurrealtygroup.com</li>
      <li>fb/me/larkspurrealtygroup</li>
      <li>@LarkspurRltyGrp</li>
    </ul>

    <div class="badges">
      <div class="badge" role="img" aria-label="Realtor membership badge"></div>
      <div class="badge" role="img" aria-label="Fair housing badge"></div>
    </div>
  </section>
</body>
</html>
```